Business Card Design

Please use the Logo for colors and styles, and create a business card using the following info:

Matthias Loeber
Web Developer

Loeber Solutions
+41 76 482 17 05
matthias@loeber-solutions.example
www.loeber-solutions.example

Download the logo at http://loeber-solutions.example/tl_files/loeber_solutions.zip

Thanks for your works!

```html
<!DOCTYPE html>
<html lang="en">
<head>
<meta charset="utf-8">
<title>Loeber Solutions – Business Card</title>
<link rel="stylesheet" href="https://fonts.googleapis.com/css2?family=Jost:wght@400;500&display=swap">
<style>
  :root {
    --backdrop: #a9abae;
    --brand-blue: #0b63a8;
    --brand-blue-deep: #08548f;
    --card-white: #f4f5f6;
    --circle-white: #eceef0;
    --circle-blue: #0e6cb5;
    --ink-grey: #4b4f55;
    --ink-white: #ffffff;
  }
  html, body {
    margin: 0;
    padding: 0;
    overflow: hidden;
  }
  body {
    width: 1200px;
    height: 900px;
    background: var(--backdrop);
    font-family: "Jost", "Futura", sans-serif;
    position: relative;
  }
  .card {
    position: absolute;
    width: 580px;
    height: 330px;
    border-radius: 26px;
    overflow: hidden;
    box-shadow: 0 10px 24px rgba(0, 0, 0, 0.22);
  }
  .card-front {
    left: 120px;
    top: 90px;
    background: linear-gradient(160deg, var(--brand-blue) 0%, var(--brand-blue-deep) 100%);
  }
  .card-back {
    left: 500px;
    top: 470px;
    background: var(--card-white);
  }
  .card-circle {
    position: absolute;
    border-radius: 50%;
  }
  .card-front .card-circle {
    width: 300px;
    height: 300px;
    right: -20px;
    top: -40px;
    background: var(--circle-blue);
  }
  .card-back .card-circle {
    width: 280px;
    height: 280px;
    right: -10px;
    top: -50px;
    background: var(--circle-white);
  }
  .brand-name {
    font-weight: 500;
    letter-spacing: 0.02em;
    text-transform: uppercase;
    white-space: nowrap;
    margin: 0;
  }
  .card-front .brand-name {
    position: absolute;
    left: 28px;
    bottom: 26px;
    transform-origin: left bottom;
    transform: rotate(-90deg) translateY(100%);
    color: var(--ink-white);
    font-size: 24px;
  }
  .holder {
    position: absolute;
    right: 70px;
    top: 82px;
    text-align: right;
  }
  .holder-name {
    margin: 0;
    font-size: 22px;
    font-weight: 500;
    color: var(--brand-blue);
  }
  .holder-role {
    margin: 0;
    font-size: 14px;
    color: var(--ink-grey);
  }
  .card-back .brand-name {
    position: absolute;
    left: 34px;
    top: 232px;
    color: var(--brand-blue);
    font-size: 32px;
  }
  .contact-line {
    position: absolute;
    left: 34px;
    top: 282px;
    margin: 0;
    font-size: 12px;
    color: var(--ink-grey);
    white-space: nowrap;
  }
  .contact-line .divider {
    margin: 0 5px;
  }
</style>
</head>
<body>
  <section class="card card-front" aria-label="Business card front">
    <div class="card-circle"></div>
    <p class="brand-name">Loeber Solutions</p>
  </section>

  <section class="card card-back" aria-label="Business card back">
    <div class="card-circle"></div>
    <div class="holder">
      <p class="holder-name">Matthias Loeber</p>
      <p class="holder-role">Web Developer</p>
    </div>
    <p class="brand-name">Loeber Solutions</p>
    <p class="contact-line">
      <span class="phone">+41 76 482 17 05</span><span class="divider">|</span><span class="email">matthias@loeber-solutions.example</span><span class="divider">|</span><span class="web">www.loeber-solutions.example</span>
    </p>
  </section>
</body>
</html>
```